TovaLamarpe - Israeli Mental Health Website

We are developing an Israeli website for mental health. The website will be both in English and in Hebrew. We have a logo and would like a website design based on the logo and the logos colors (attached).

Attached is a doc that contains the website requirements.

We would like to have an icon for each of the sidebar categories, an image for each of the pages (including each of the sidebar category pages).

Target Market(s)

Adults 18-80

Industry/Entity Type

Mental Health

Number of Pages Required

5+ page

Font styles to use
Sans Serif

Colors

Designer to choose colors to be used in the design.

```html
<!DOCTYPE html>
<html lang="en">
<head>
<meta charset="utf-8">
<title>TovaLamarpe – Organizations</title>
<link href="https://fonts.googleapis.com/css2?family=Poppins:wght@400;500;600;700&display=swap" rel="stylesheet">
<style>
:root{
  --blue:#2373bd;
  --green:#4ca93d;
  --ink:#2b2b2b;
  --muted:#777;
  --field:#ececec;
  --pale-blue:#bcd4ec;
  --white:#fff;
}
*{box-sizing:border-box;margin:0;padding:0}
html,body{width:747px;height:1200px;overflow:hidden;background:var(--white);font-family:'Poppins',sans-serif;color:var(--ink)}
.page{position:relative;width:747px;height:1200px}
.abs{position:absolute}

.brand{left:26px;top:14px;display:flex;align-items:center;gap:7px}
.brand-dot{width:26px;height:26px;border-radius:50%;background:var(--blue)}
.brand-name{font-size:17px;font-weight:600;color:var(--blue)}

.lang{left:565px;top:20px;display:flex;align-items:center;gap:4px;font-size:9px}
.lang-dot{width:14px;height:14px;border-radius:50%;background:linear-gradient(#c8283c 50%,#2b3e8f 50%)}
.get-help{left:634px;top:12px;width:84px;height:29px;border-radius:15px;background:var(--green);color:var(--white);font-size:8.5px;font-weight:700;display:flex;align-items:center;justify-content:center}

.nav{top:52px;left:240px;right:28px;display:flex;justify-content:space-between;font-size:9.3px;font-weight:500}
.nav .active{color:var(--green)}

.intro-title{left:54px;top:203px;font-size:17.5px;font-weight:700;color:var(--blue)}
.intro-text{left:55px;top:236px;width:285px;font-size:9.8px;line-height:13.8px}

.hero-photo{left:369px;top:123px;width:322px;height:322px;border-radius:50%;background:radial-gradient(circle at 50% 30%,#f7d79a,#e3a24d 45%,#6b5a4a 75%,#3a3430)}

.filter{top:497px;width:109px}
.filter label{display:block;font-size:8.3px;font-weight:600;margin-bottom:8px}
.select{height:30px;border-radius:15px;background:var(--field);font-size:8px;color:var(--muted);padding:0 14px 0 18px;display:flex;align-items:center;justify-content:space-between}
.select svg{width:7px;height:5px}
.search{left:618px;top:514px;width:85px;height:29px;border-radius:15px;background:var(--green);color:var(--white);font-size:8.5px;font-weight:700;display:flex;align-items:center;justify-content:center}

.card{top:592px;width:150px;height:223px;border-radius:8px;background:var(--white);box-shadow:0 8px 22px rgba(0,0,0,.09);overflow:hidden}
.card-photo{height:129px}
.card-body{padding:10px 15px}
.card-name{font-size:11px;font-weight:600}
.card-role{font-size:7.3px;color:var(--muted);font-weight:500;margin-top:2px}
.card-text{font-size:8.3px;line-height:11px;margin-top:8px}

.suggest{left:0;width:747px;top:865px;text-align:center;font-size:17px;font-weight:700;color:var(--blue)}
.contact{left:331px;top:894px;width:85px;height:34px;border-radius:17px;background:var(--green);color:var(--white);font-size:8.5px;font-weight:700;display:flex;align-items:center;justify-content:center}

.wave{left:0;top:936px;width:747px;height:264px}
.footer-brand{left:0;width:747px;top:1055px;display:flex;flex-direction:column;align-items:center;gap:10px}
.footer-dot{width:56px;height:56px;border-radius:50%;border:3px solid var(--white)}
.footer-name{font-size:26px;font-weight:600;color:var(--white)}
.chat-float{left:671px;top:1049px;width:42px;height:42px;border-radius:50%;background:var(--green);border:2px solid var(--white)}
.footer-rule{left:56px;top:1168px;width:636px;height:1px;background:rgba(255,255,255,.35)}
.copyright{left:0;width:747px;top:1178px;text-align:center;font-size:9px;color:var(--white)}
.legal{right:54px;top:1178px;font-size:9px;color:var(--white);display:flex;gap:7px}
</style>
</head>
<body>
<div class="page">

  <div class="abs brand"><span class="brand-dot"></span><span class="brand-name">TovaLamarpe</span></div>
  <div class="abs lang"><span class="lang-dot"></span>English
    <svg width="7" height="5" viewBox="0 0 7 5"><path d="M1 1l2.5 2.5L6 1" fill="none" stroke="#2b2b2b" stroke-width="1.2"/></svg></div>
  <div class="abs get-help">GET HELP</div>

  <nav class="abs nav">
    <span>Categories ⌄</span><span>Smart Chat</span><span>Therapists</span>
    <span class="active">Organization</span><span>Videos</span><span>Donate</span><span>Contact</span><span>About</span>
  </nav>

  <h1 class="abs intro-title">Organizations</h1>
  <p class="abs intro-text">Lorem ipsum dolor sit amet, consectetur adipiscing elit, sed do eiusmod tempor incididunt ut labore et dolore magna aliqua. Ut enim ad minim veniam, quis nostrud exercitation ullamco laboris nisi ut aliquip ex ea commodo consequat. Duis aute irure dolor in reprehenderit in voluptate velit esse cillum dolore eu fugiat nulla pariatur. Excepteur sint occaecat cupidatat non proident, sunt in culpa qui officia deserunt mollit anim id est laborum</p>

  <div class="abs hero-photo" role="img" aria-label="Four friends embracing, seen from behind, facing a golden sunset"></div>

  <div class="abs filter" style="left:44px"><label>Area</label><div class="select">City 1<svg viewBox="0 0 7 5"><path d="M1 1l2.5 2.5L6 1" fill="none" stroke="#444" stroke-width="1.2"/></svg></div></div>
  <div class="abs filter" style="left:159px"><label>Category</label><div class="select">General<svg viewBox="0 0 7 5"><path d="M1 1l2.5 2.5L6 1" fill="none" stroke="#444" stroke-width="1.2"/></svg></div></div>
  <div class="abs filter" style="left:273px"><label>Sub-Category</label><div class="select">SubCategory 1<svg viewBox="0 0 7 5"><path d="M1 1l2.5 2.5L6 1" fill="none" stroke="#444" stroke-width="1.2"/></svg></div></div>
  <div class="abs filter" style="left:388px"><label>Payment</label><div class="select">Subsidized<svg viewBox="0 0 7 5"><path d="M1 1l2.5 2.5L6 1" fill="none" stroke="#444" stroke-width="1.2"/></svg></div></div>
  <div class="abs filter" style="left:502px"><label>Therapist Gender</label><div class="select">Man<svg viewBox="0 0 7 5"><path d="M1 1l2.5 2.5L6 1" fill="none" stroke="#444" stroke-width="1.2"/></svg></div></div>
  <div class="abs search">SEARCH</div>

  <article class="abs card" style="left:139px">
    <div class="card-photo" role="img" aria-label="Therapist in a striped shirt at his office" style="background:linear-gradient(135deg,#c9cfd6,#8fa6c4)"></div>
    <div class="card-body"><div class="card-name">Daniel Oren</div><div class="card-role">Psychologist</div>
      <p class="card-text">Lorem ipsum dolor sit amet consectetur adipiscing elit sed do eiusmod tempor...</p></div>
  </article>
  <article class="abs card" style="left:298px">
    <div class="card-photo" role="img" aria-label="Smiling therapist with glasses at a laptop" style="background:linear-gradient(135deg,#b9c4c8,#5d7080)"></div>
    <div class="card-body"><div class="card-name">Yoni Katzir</div><div class="card-role">Psychiatrist</div>
      <p class="card-text">Lorem ipsum dolor sit amet consectetur adipiscing elit sed do eiusmod tempor...</p></div>
  </article>
  <article class="abs card" style="left:458px">
    <div class="card-photo" role="img" aria-label="Therapist in a light blue shirt reading at his desk" style="background:linear-gradient(135deg,#e4e8ec,#a9c3dc)"></div>
    <div class="card-body"><div class="card-name">Ari Mendelo</div><div class="card-role">Psychoanalyst</div>
      <p class="card-text">Lorem ipsum dolor sit amet consectetur adipiscing elit sed do eiusmod tempor...</p></div>
  </article>

  <h2 class="abs suggest">Do you have any suggestions?</h2>
  <div class="abs contact">CONTACT US</div>

  <svg class="abs wave" viewBox="0 0 747 264" preserveAspectRatio="none" aria-hidden="true">
    <path d="M0 10 C90 60 210 70 355 40 C250 80 120 80 0 55Z" fill="var(--pale-blue)"/>
    <path d="M0 55 C140 120 300 105 440 60 C560 18 680 10 747 45 V264 H0Z" fill="var(--green)"/>
    <path d="M0 55 C140 125 290 120 420 78 C560 35 680 30 747 75 V264 H0Z" fill="var(--blue)"/>
  </svg>

  <div class="abs footer-brand"><span class="footer-dot"></span><span class="footer-name">TovaLamarpe</span></div>
  <div class="abs chat-float"></div>
  <div class="abs footer-rule"></div>
  <div class="abs copyright">TovaLamarpe-Organization for Mental Health ©2023</div>
  <div class="abs legal"><span>Privacy Policy</span><span>Terms</span></div>

</div>
</body>
</html>
```